Quorvel Landing page redesign

We are looking for a landing page redesign before we officially launch. We want to incorporate the information already on the site at www.Quorvel-example.com landing page but make it more inviting. There needs to be a sign up section along with clearly stating what we do. Having a place for sample profiles and linking to our blog and podcast is option. More information about all we will be doing is at Quorvel is on the landing page and also on the blog.

Target Market(s)

35 years old and up.

Coding

Coded - Design and coding required

Number of Pages Required

1 page

Requirements
Must have
• The top bar and the bottom bar (with the privacy policy, etc)
• Sign in/up section.
• I don't want to give to much here because I want designers to be creative.
Nice to have
• Prefer not to have a landing page that requires a lot of scrolling at all.

```html
<!DOCTYPE html>
<html lang="en">
<head>
<meta charset="utf-8">
<title>Quorvel</title>
<link href="https://fonts.googleapis.com/css2?family=Roboto:wght@300;400;500;700&display=swap" rel="stylesheet">
<style>
:root{
  --navy:#1b1f6b;
  --navy-deep:#161a5c;
  --sky:#0b96e8;
  --ink:#222;
  --muted:#666;
  --faint:#999;
  --line:#d9d9d9;
  --foot:#f0f0f0;
  --white:#fff;
}
*{box-sizing:border-box;margin:0;padding:0}
html,body{width:929px;height:1200px;overflow:hidden;background:var(--white);font-family:"Roboto",sans-serif;color:var(--ink)}
.page{position:relative;width:929px;height:1200px}

/* top bar */
.topbar{position:absolute;left:0;top:0;width:929px;height:42px;background:var(--white);z-index:3}
.brand{position:absolute;left:70px;top:12px;font-size:15px;font-weight:500;color:var(--navy-deep)}
.nav{position:absolute;right:70px;top:10px;display:flex;align-items:center;gap:19px;font-size:10px}
.nav a{color:var(--ink);text-decoration:none}
.nav .login{background:var(--sky);color:var(--white);width:56px;height:23px;display:flex;align-items:center;justify-content:center}

/* hero */
.hero-bg{position:absolute;left:0;top:42px;width:929px;height:440px}
.hero-title{position:absolute;left:0;width:929px;text-align:center;top:122px;font-size:25px;color:var(--white);font-weight:400}
.hero-sub{position:absolute;left:0;width:929px;text-align:center;top:157px;font-size:10px;line-height:14.5px;color:var(--white)}
.btn-sample{position:absolute;left:346px;top:195px;width:126px;height:28px;background:var(--white);font-size:10px;display:flex;align-items:center;justify-content:center;color:var(--ink)}
.link-sample{position:absolute;left:486px;top:204px;font-size:10px;color:var(--white);text-decoration:underline}

/* connections preview */
.back-card{position:absolute;left:260px;top:298px;width:409px;height:203px;background:var(--white);border:1px solid var(--line)}
.back-card .band{height:33px;background:#a9a9ae}
.front-card{position:absolute;left:284px;top:253px;width:361px;height:268px;background:var(--white);border:1px solid var(--line)}
.front-card .bar{height:35px;background:var(--sky);display:flex;align-items:center;padding-left:21px;gap:3px}
.front-card .bar i{width:7px;height:7px;border-radius:50%;background:var(--white)}
.panel-title{text-align:center;font-size:12px;margin-top:8px;padding-bottom:6px;border-bottom:1px solid #eee;margin-left:6px;margin-right:6px}
.group{position:absolute;top:69px;width:110px}
.group h4{font-weight:400;font-size:9px;color:#444;margin-bottom:14px}
.person{display:flex;align-items:center;height:20px;margin-bottom:5px}
.avatar{width:20px;height:20px;margin-right:9px;flex:none}
.person b{display:block;font-size:6px;font-weight:500;color:var(--navy)}
.person small{display:block;font-size:4.5px;color:var(--faint);font-style:italic}
.add-btn{position:absolute;left:112px;top:226px;width:127px;height:21px;background:var(--navy-deep);color:var(--white);font-size:11px;display:flex;align-items:center;justify-content:center;gap:6px}
.arrow-btn{position:absolute;top:389px;width:26px;height:26px;border-radius:50%;background:#1a1d55;display:flex;align-items:center;justify-content:center}

/* early user */
.divider{position:absolute;left:465px;top:575px;width:1px;height:158px;background:var(--line)}
.signup-title{position:absolute;left:193px;width:229px;text-align:center;top:595px;font-size:18px;font-weight:400}
.email{position:absolute;left:193px;top:626px;width:229px;height:33px;border:1px solid var(--line);font-size:9.5px;color:var(--faint);padding-left:12px;display:flex;align-items:center}
.subscribe{position:absolute;left:193px;top:663px;width:229px;height:33px;background:var(--sky);color:var(--white);font-size:12px;display:flex;align-items:center;justify-content:center}
.already{position:absolute;left:193px;width:229px;text-align:center;top:704px;font-size:9.5px}
.already a{color:var(--sky);text-decoration:none}
.features{position:absolute;left:514px;top:601px;list-style:none;font-size:10.5px;line-height:19.3px;color:var(--muted)}
.features b{font-weight:400;color:var(--ink)}

/* blog */
.blog-title{position:absolute;left:0;width:929px;text-align:center;top:771px;font-size:22px;font-weight:400}
.post{position:absolute;top:819px;width:251px}
.post .photo{width:251px;height:169px;clip-path:polygon(0 0,100% 0,72% 100%,0 100%)}
.post .cal{position:absolute;left:214px;top:31px;width:31px;height:31px;display:flex;align-items:center;justify-content:center}
.post .date{position:absolute;left:214px;top:113px;width:31px;text-align:center;font-size:8.5px;line-height:13.5px;color:var(--faint)}
.post .date b{font-weight:400;color:var(--ink)}
.post h3{position:absolute;top:182px;left:-1px;width:260px;font-weight:400;font-size:11.5px;color:#333}

/* footer */
.footer{position:absolute;left:0;top:1063px;width:929px;height:102px;background:var(--foot)}
.foot-brand{position:absolute;left:0;width:929px;top:30px;text-align:center;color:var(--navy-deep);font-weight:500;font-size:22px}
.foot-links{position:absolute;left:0;width:929px;top:66px;text-align:center;font-size:9.5px;color:#333}
.foot-links span{margin:0 10px}
.copybar{position:absolute;left:0;top:1165px;width:929px;height:35px;background:var(--navy-deep);color:var(--white);font-size:9.5px;display:flex;align-items:center;justify-content:center}
.to-top{position:absolute;left:879px;top:1153px;width:23px;height:23px;border-radius:50%;background:var(--sky);display:flex;align-items:center;justify-content:center;z-index:4}
</style>
</head>
<body>
<div class="page">

  <header class="topbar">
    <div class="brand">Quorvel</div>
    <nav class="nav"><a href="#">Blog</a><a href="#">Podcast</a><a class="login" href="#">Login</a></nav>
  </header>

  <svg class="hero-bg" viewBox="0 0 929 440" preserveAspectRatio="none">
    <defs>
      <radialGradient id="heroGlow" cx="50%" cy="15%" r="70%">
        <stop offset="0" stop-color="#34459c"/>
        <stop offset="1" stop-color="#1a1f6e"/>
      </radialGradient>
    </defs>
    <path d="M0 0H929V378Q464.5 500 0 378Z" fill="url(#heroGlow)"/>
  </svg>

  <h1 class="hero-title">Quorvel Pages</h1>
  <p class="hero-sub">Build multiple Quorvel pages through one account for yourself, your family and<br>to keep loved one's legacies alive.</p>
  <a class="btn-sample">Sample Quorvel Profile</a>
  <a class="link-sample">Sample Legacy Profile</a>

  <div class="back-card"><div class="band"></div></div>
  <div class="front-card">
    <div class="bar"><i></i><i></i><i></i></div>
    <div class="panel-title">Family &amp; Friends</div>

    <div class="group" style="left:22px">
      <h4>Family</h4>
      <div class="person"><div class="avatar" role="img" aria-label="Profile photo" style="background:#7a5a48"></div><div><b>Owen Marlowe</b><small>Brother</small></div></div>
      <div class="person"><div class="avatar" role="img" aria-label="Profile photo" style="background:#8c6a5c"></div><div><b>Clara Marlowe</b><small>Sister</small></div></div>
      <div class="person" style="margin-top:6px"><div class="avatar" role="img" aria-label="Profile photo" style="background:#9a7e6a"></div><div><b>Nadia Ferrin</b><small>Aunt</small></div></div>
      <div class="person"><div class="avatar" role="img" aria-label="Profile photo" style="background:#8f8a7c"></div><div><b>Hilda Strand</b><small>Grandmother</small></div></div>
    </div>

    <div class="group" style="left:127px">
      <h4>Friends — Growing Up</h4>
      <div class="person"><div class="avatar" role="img" aria-label="Profile photo" style="background:#6f6258"></div><div><b>Jonah Pell</b><small>Oldest friend</small></div></div>
      <div class="person"><div class="avatar" role="img" aria-label="Profile photo" style="background:#5e5a5c"></div><div><b>Miles Arden</b><small>Cousin pal</small></div></div>
      <div class="person" style="margin-top:6px"><div class="avatar" role="img" aria-label="Profile photo" style="background:#4e4a48"></div><div><b>Toby Lund</b><small>Neighbor</small></div></div>
    </div>

    <div class="group" style="left:258px">
      <h4>Friends — College</h4>
      <div class="person"><div class="avatar" role="img" aria-label="Profile photo" style="background:#7c6558"></div><div><b>Evan Kerr</b><small>Pledge Brother</small></div></div>
      <div class="person"><div class="avatar" role="img" aria-label="Profile placeholder" style="background:#c9c9c9"></div><div><b>Dean Colby <span style="font-weight:400;color:#999;font-size:4.5px">— PENDING</span></b><small>Pledge Brother</small></div></div>
    </div>

    <div class="add-btn">
      <svg width="11" height="11" viewBox="0 0 11 11"><path d="M5.5 0V11M0 5.5H11" stroke="#fff" stroke-width="1.4"/></svg>
      Add Connection
    </div>
  </div>

  <div class="arrow-btn" style="left:226px"><svg width="8" height="8" viewBox="0 0 8 8"><path d="M5 1.5 2.5 4 5 6.5" fill="none" stroke="#fff" stroke-width="1.2"/></svg></div>
  <div class="arrow-btn" style="left:679px"><svg width="8" height="8" viewBox="0 0 8 8"><path d="M3 1.5 5.5 4 3 6.5" fill="none" stroke="#fff" stroke-width="1.2"/></svg></div>

  <section>
    <h2 class="signup-title">Become an Early User</h2>
    <div class="email">Type your email address</div>
    <div class="subscribe">Subscribe</div>
    <p class="already">Already Have an Account? <a href="#">Sign in</a></p>
    <div class="divider"></div>
    <ul class="features">
      <li><b>Create</b> Timelines, Maps, Family Trees</li>
      <li><b>Memorialize</b> Loved Ones</li>
      <li><b>Share</b> Family Stories, History and more</li>
      <li><b>Control</b> Your Privacy</li>
      <li><b>No</b> Ads, No Like Buttons</li>
      <li><b>No</b> News Feeds</li>
    </ul>
  </section>

  <h2 class="blog-title">Latest Blog</h2>

  <article class="post" style="left:69px">
    <div class="photo" role="img" aria-label="Black and white photo of a grandparent holding a newborn" style="background:linear-gradient(135deg,#4a4a4a,#bdbdbd 60%,#8a8a8a)"></div>
    <div class="cal" style="background:var(--navy-deep)"><svg width="11" height="11" viewBox="0 0 11 11"><rect x="0.5" y="1.5" width="10" height="9" fill="none" stroke="#fff"/><rect x="0.5" y="1.5" width="10" height="2.5" fill="#fff"/><path d="M2.5 6h1M5 6h1M7.5 6h1M2.5 8h1M5 8h1M7.5 8h1" stroke="#fff"/></svg></div>
    <div class="date"><b>18</b><br>May<br>2016</div>
    <h3>Using Legacy Organize Your Family History</h3>
  </article>

  <article class="post" style="left:336px">
    <div class="photo" role="img" aria-label="Black and white photo of a mother holding a baby" style="background:linear-gradient(135deg,#cfcfcf,#5a5a5a 55%,#9a9a9a)"></div>
    <div class="cal" style="background:var(--sky)"><svg width="11" height="11" viewBox="0 0 11 11"><rect x="0.5" y="1.5" width="10" height="9" fill="none" stroke="#fff"/><rect x="0.5" y="1.5" width="10" height="2.5" fill="#fff"/><path d="M2.5 6h1M5 6h1M7.5 6h1M2.5 8h1M5 8h1M7.5 8h1" stroke="#fff"/></svg></div>
    <div class="date"><b>15</b><br>June<br>2016</div>
    <h3>Creating Context for Your Family History</h3>
  </article>

  <article class="post" style="left:608px">
    <div class="photo" role="img" aria-label="Black and white photo of a man before a wall of theatre posters" style="background:linear-gradient(135deg,#7a7a7a,#3e3e3e 50%,#b0b0b0)"></div>
    <div class="cal" style="background:var(--navy-deep)"><svg width="11" height="11" viewBox="0 0 11 11"><rect x="0.5" y="1.5" width="10" height="9" fill="none" stroke="#fff"/><rect x="0.5" y="1.5" width="10" height="2.5" fill="#fff"/><path d="M2.5 6h1M5 6h1M7.5 6h1M2.5 8h1M5 8h1M7.5 8h1" stroke="#fff"/></svg></div>
    <div class="date"><b>3</b><br>Jan<br>2016</div>
    <h3>Quorvel Podcast – Episode 5</h3>
  </article>

  <footer class="footer">
    <div class="foot-brand">Quorvel</div>
    <p class="foot-links">Privacy Policy<span>|</span>Terms of Use<span>|</span>Data Tracking Policy<span>|</span>Submit Feedback</p>
  </footer>
  <div class="to-top"><svg width="8" height="8" viewBox="0 0 8 8"><path d="M1.5 5 4 2.5 6.5 5" fill="none" stroke="#fff" stroke-width="1.3"/></svg></div>
  <div class="copybar">Quorvel © 2017 | All Right Reserved</div>

</div>
</body>
</html>
```